Business card design

Hi I'm needing my business cards redesigned

COMPANY NAME MOP HARBOR
email mopharbor.official@
mobile phone 01157302818
FB page & IG: MOP HARBOR

black and white logo theme
background color of the card yellow
OUR SLOGAN IS "Together We Strong"

```html
<!DOCTYPE html>
<html lang="en">
<head>
<meta charset="utf-8">
<title>MOP HARBOR — Business Card</title>
<link href="https://fonts.googleapis.com/css2?family=Oswald:wght@600&family=Lato:wght@300;400;700&display=swap" rel="stylesheet">
<style>
  :root {
    --page: #3d3f42;
    --yellow: #f9b712;
    --yellow-light: #fcc72a;
    --orange: #f2921a;
    --black: #0d0d0d;
    --white: #ffffff;
    --stripe: #ececec;
    --ink: #2b2b2b;
    --icon: #3a3f45;
    --brown: #2a1a17;
  }
  * { box-sizing: border-box; margin: 0; padding: 0; }
  html, body { width: 1200px; height: 900px; overflow: hidden; }
  body {
    background: var(--page);
    position: relative;
    font-family: "Lato", sans-serif;
  }
  .card {
    position: absolute;
    width: 560px;
    height: 320px;
    overflow: hidden;
    box-shadow: 0 12px 30px rgba(0,0,0,0.35);
  }

  /* Front */
  .card-front { left: 110px; top: 90px; background: linear-gradient(120deg, var(--yellow-light), var(--yellow)); }
  .front-stripe { position: absolute; left: 0; right: 0; top: 88px; height: 18px; background: var(--stripe); }
  .front-band { position: absolute; left: 0; right: 0; top: 106px; height: 118px; background: var(--black); }
  .front-brand { position: absolute; left: 48px; top: 126px; display: flex; align-items: center; gap: 16px; }
  .brand-mark { width: 62px; height: 62px; background: var(--yellow); flex: none; }
  .brand-text { display: flex; flex-direction: column; }
  .front-name { font-family: "Oswald", sans-serif; font-weight: 600; font-size: 46px; line-height: 1; color: var(--white); letter-spacing: 1px; }
  .front-slogan { font-family: "Lato", sans-serif; font-weight: 400; font-size: 24px; color: var(--white); margin-top: 4px; }

  /* Back */
  .card-back { left: 530px; top: 480px; }
  .card-back svg.back-bg { position: absolute; inset: 0; }
  .back-brand { position: absolute; left: 160px; top: 92px; display: flex; align-items: center; gap: 10px; }
  .back-brand .mark { width: 30px; height: 30px; border-radius: 4px; background: var(--orange); }
  .back-name { font-family: "Lato", sans-serif; font-weight: 700; font-size: 24px; color: var(--ink); }
  .icon-box {
    position: absolute; width: 38px; height: 38px; border-radius: 7px;
    background: var(--icon); border: 2px solid var(--white);
    display: flex; align-items: center; justify-content: center;
  }
  .icon-social { left: 58px; top: 200px; }
  .icon-phone { left: 268px; top: 162px; }
  .icon-mail { left: 444px; top: 118px; }
  .contact { position: absolute; font-family: "Lato", sans-serif; color: var(--ink); white-space: nowrap; }
  .contact-social { left: 38px; top: 254px; font-size: 13px; }
  .contact-phone { left: 218px; top: 222px; font-size: 14px; letter-spacing: 3px; }
  .contact-mail { left: 358px; top: 168px; font-size: 12px; }
</style>
</head>
<body>

  <section class="card card-front" aria-label="Business card front">
    <div class="front-stripe"></div>
    <div class="front-band"></div>
    <div class="front-brand">
      <div class="brand-mark"></div>
      <div class="brand-text">
        <span class="front-name">MOP HARBOR</span>
        <span class="front-slogan">Together We Strong</span>
      </div>
    </div>
  </section>

  <section class="card card-back" aria-label="Business card back">
    <svg class="back-bg" width="560" height="320" viewBox="0 0 560 320">
      <defs>
        <linearGradient id="backYellow" x1="0" y1="0" x2="1" y2="1">
          <stop offset="0" stop-color="#fcc72a"/>
          <stop offset="1" stop-color="#f4aa14"/>
        </linearGradient>
      </defs>
      <rect width="560" height="320" fill="url(#backYellow)"/>
      <polygon points="0,190 560,150 560,255 0,290" fill="#ffffff"/>
      <polygon points="440,158 560,150 560,200 440,205" fill="url(#backYellow)"/>
      <polygon points="250,272 390,262 390,320 250,320" fill="#2a1a17"/>
      <polygon points="390,262 560,250 560,320 390,320" fill="url(#backYellow)"/>
    </svg>

    <div class="back-brand">
      <div class="mark"></div>
      <span class="back-name">MOP HARBOR</span>
    </div>

    <div class="icon-box icon-social"></div>
    <div class="icon-box icon-phone">
      <svg width="20" height="20" viewBox="0 0 24 24" aria-hidden="true">
        <circle cx="12" cy="12" r="10" fill="none" stroke="#fff" stroke-width="1.6"/>
        <path d="M8.5 7.5c-.6.6-.8 1.6-.3 2.9 1 2.3 2.8 4.1 5.1 5.1 1.3.5 2.3.3 2.9-.3l.5-.6-2-1.6-1 .8c-1.2-.6-2.2-1.6-2.8-2.8l.8-1-1.6-2z" fill="#fff"/>
      </svg>
    </div>
    <div class="icon-box icon-mail">
      <svg width="20" height="16" viewBox="0 0 20 16" aria-hidden="true">
        <rect x="1" y="1" width="18" height="14" rx="1" fill="none" stroke="#fff" stroke-width="1.6"/>
        <path d="M1 1l9 8 9-8" fill="none" stroke="#fff" stroke-width="1.6"/>
      </svg>
    </div>

    <span class="contact contact-social">MOP HARBOR</span>
    <span class="contact contact-phone">01157302818</span>
    <span class="contact contact-mail">mopharbor.official@harbormail.com</span>
  </section>

</body>
</html>
```